Timber Ridge Land Services Business Cards

Need to create a business card with the company logo "Timber Ridge Land Services". The business will provide forestry mulching for land clearing and vegetation control, brush and small tree removal, wildlife habitat improvement and trail and property access creation.

```html
<!DOCTYPE html>
<html lang="en">
<head>
<meta charset="UTF-8">
<title>Timber Ridge Land Services – Business Card</title>
<link href="https://fonts.googleapis.com/css2?family=Russo+One&family=Poppins:wght@400;500&display=swap" rel="stylesheet">
<style>
  :root {
    --forest: #025c4b;
    --leaf: #6cc167;
    --ink: #1c1c1c;
    --card: #f6f4f3;
    --backdrop: #e4e2e0;
  }
  * { margin: 0; padding: 0; box-sizing: border-box; }
  html, body {
    width: 1200px; height: 900px; overflow: hidden;
    background: var(--backdrop);
  }
  .card {
    position: absolute; left: 100px; top: 140px;
    width: 1000px; height: 620px;
    background: var(--card);
    overflow: hidden;
    box-shadow: 0 12px 40px rgba(0,0,0,0.15);
  }
  .person { position: absolute; left: 58px; top: 78px; }
  .person-name {
    font-family: "Russo One", sans-serif;
    font-size: 43px; line-height: 1; letter-spacing: 0.5px;
    color: var(--forest); text-transform: uppercase;
  }
  .person-title {
    font-family: "Poppins", sans-serif;
    font-size: 28px; color: var(--ink); margin-top: 2px;
  }
  .contact-list {
    position: absolute; left: 60px; top: 188px; list-style: none;
    font-family: "Poppins", sans-serif; font-size: 28px; color: var(--ink);
  }
  .contact-list li { display: flex; align-items: center; height: 37px; }
  .contact-icon { width: 26px; height: 26px; margin-right: 10px; flex: none; }
  .contact-icon--solid { fill: var(--forest); }
  .contact-icon--line { fill: none; stroke: var(--forest); stroke-width: 1.8; }
  .address {
    position: absolute; left: 62px; top: 324px;
    font-family: "Poppins", sans-serif; font-size: 29px; line-height: 37px; color: var(--ink);
  }
  .brand {
    position: absolute; left: 560px; top: 268px; width: 380px;
    text-align: center;
    font-family: "Poppins", sans-serif; font-weight: 500;
    font-size: 30px; line-height: 1.25;
    color: var(--forest);
  }
  .footer-band {
    position: absolute; left: 0; bottom: 0; width: 1000px; height: 110px;
    background: var(--forest);
    border-top: 10px solid var(--leaf);
  }
</style>
</head>
<body>
  <div class="card">
    <div class="person">
      <h1 class="person-name">Daniel Carter</h1>
      <p class="person-title">Managing Director</p>
    </div>

    <ul class="contact-list">
      <li>
        <svg class="contact-icon contact-icon--solid" viewBox="0 0 24 24" aria-hidden="true"><path d="M6.6 10.8a15.1 15.1 0 0 0 6.6 6.6l2.2-2.2a1 1 0 0 1 1-.25 11.4 11.4 0 0 0 3.6.57 1 1 0 0 1 1 1V20a1 1 0 0 1-1 1A17 17 0 0 1 3 4a1 1 0 0 1 1-1h3.5a1 1 0 0 1 1 1c0 1.25.2 2.45.57 3.57a1 1 0 0 1-.25 1z"/></svg>
        044-555 210 736
      </li>
      <li>
        <svg class="contact-icon contact-icon--solid" viewBox="0 0 24 24" aria-hidden="true"><path d="M2 5h20v14H2z"/><path d="M3 6l9 7 9-7" fill="none" stroke="#fff" stroke-width="1.4"/></svg>
        info@timberridgeland.com
      </li>
      <li>
        <svg class="contact-icon contact-icon--line" viewBox="0 0 24 24" aria-hidden="true"><circle cx="12" cy="12" r="9.5"/><ellipse cx="12" cy="12" rx="4.2" ry="9.5"/><path d="M2.5 12h19M4 7h16M4 17h16"/></svg>
        www.timberridgeland.com
      </li>
    </ul>

    <p class="address">88, Cedar Hollow Road<br>Millbrook 60317, Country</p>

    <p class="brand">Timber Ridge<br>Land Services</p>

    <div class="footer-band" aria-hidden="true"></div>
  </div>
</body>
</html>
```